Corvane Electrical Services Website

'Marlcombe Electrical Services' is a leading electrician company based in Hertfordshire. We are a DRUVIK approved and registered company in the UK. We are also registered to carry out electrical installations under Part P of the building regulations. As part of a wide range of electrical services, we have professional expertise in installation testing (landlords, periodic, insurance, emergency lighting & fire alarms) rewires, installations, electrical maintenance, security systems & portable appliance testing (PAT). We provide a bespoke service to suite the needs of High End clients so the site must reflect the type of clientele we are targeting

WE ARE A SMALL COMPANY AND ARE LOOKING FOR THE DESIGNERS TO ALSO IMPLEMENT THIS ONTO OUR DOMAIN NAME SO ITS A FULLY FUNCTIONAL FOR OUR CLIENTS WHEN WE FINISH THIS SIMPLE PROJECT

Target Market(s)

Estate Agents, High End Clients that require intallations in Multi Million pound houses

Industry/Entity Type

Electrician

Font styles to use
Serif
Sans Serif
Other font styles liked:
• Chose an elegant professional font

Requirements
Must have
• please look at www.marlcombeelectrical-demo.co.uk (the current old site is down, and will go live in 24-48 hours so please get the content from there)

Luxury design, a wow factor when high end clients logon

the logo is Blue so a blue colour these for the branding is essential. We are open to your design ideas around the logo.

DRUVIK and Part P and Electrical Norwin Council are safety regulations so please add the logos a place on the site together.
Nice to have
• your creative input
Should not have
• to many conflicting colours, too many horrible bright colours

```html
<!DOCTYPE html>
<html lang="en">
<head>
<meta charset="utf-8">
<title>Marlcombe Electrical Services</title>
<link href="https://fonts.googleapis.com/css2?family=Arimo:wght@400;700&display=swap" rel="stylesheet">
<style>
  :root {
    --brand-blue: #1c2a8c;
    --navy: #15215a;
    --ink: #2b2b2b;
    --muted: #555;
    --page: #f1f1f1;
    --side-light: #e6e6e6;
    --side-dark: #a9a9a9;
    --field: #dcdcdc;
    --field-edge: #bdbdbd;
    --caption-bg: rgba(20, 20, 20, 0.72);
    --link: #5fb2ff;
    --tab: #d9d9d9;
  }
  * { box-sizing: border-box; margin: 0; padding: 0; }
  html, body { width: 1200px; height: 533px; overflow: hidden; }
  body {
    font-family: "Arimo", Arial, sans-serif;
    color: var(--ink);
    background: linear-gradient(90deg, var(--side-dark) 0%, var(--side-light) 9%, var(--page) 14%, var(--page) 86%, var(--side-light) 91%, var(--side-dark) 100%);
    position: relative;
  }
  .top-rule { position: absolute; top: 0; left: 0; right: 0; height: 3px; background: var(--brand-blue); }

  .site-header { position: absolute; top: 28px; left: 200px; right: 200px; height: 70px; }
  .brand { position: absolute; left: 0; top: 18px; }
  .brand-name { display: block; font-size: 27px; font-weight: 400; color: var(--brand-blue); letter-spacing: 0.2px; }
  .brand-tagline { display: block; margin-top: 4px; font-size: 11px; font-weight: 400; color: var(--muted); letter-spacing: 0.3px; }

  .callback { position: absolute; right: 0; top: 0; width: 232px; }
  .callback p { font-size: 10px; color: var(--muted); line-height: 1.25; margin-bottom: 6px; }
  .callback-row { display: flex; align-items: center; gap: 4px; background: #d6d6d6; border-radius: 4px; padding: 4px; }
  .callback-field { height: 16px; border-radius: 8px; background: #c4c4c4; box-shadow: inset 0 1px 2px rgba(0,0,0,.25); }
  .callback-field.short { width: 46px; }
  .callback-field.long { width: 86px; }
  .callback-btn { margin-left: auto; width: 30px; height: 24px; display: flex; align-items: center; justify-content: center; border-left: 1px solid #b5b5b5; }

  .main-nav { position: absolute; top: 112px; left: 0; right: 0; display: flex; justify-content: center; gap: 36px; align-items: center; }
  .main-nav a { font-size: 19px; font-weight: 700; color: #222; text-decoration: none; padding: 6px 10px; }
  .main-nav a.active { background: linear-gradient(#3b6fe0, #1d44b0); color: #fff; border-radius: 6px; box-shadow: 0 1px 3px rgba(0,0,0,.4); }

  .hero-band { position: absolute; top: 182px; left: 0; right: 0; height: 148px; background: var(--navy); }
  .hero { position: absolute; top: 160px; left: 190px; width: 820px; height: 150px; border: 3px solid #fff; box-shadow: 0 2px 6px rgba(0,0,0,.4); overflow: hidden; }
  .hero-photo { position: absolute; inset: 0; background: linear-gradient(100deg, #7d8fa8 0%, #c9c0a6 35%, #d8d2bf 60%, #8b8a7f 100%); }
  .hero-caption { position: absolute; right: 0; top: 40px; width: 450px; padding: 8px 14px 10px; background: var(--caption-bg); color: #fff; }
  .hero-caption h2 { font-size: 26px; font-weight: 400; margin-bottom: 6px; }
  .hero-caption p { font-size: 12px; line-height: 1.3; }
  .hero-caption a { color: var(--link); }
  .hero-pager { position: absolute; top: 312px; left: 540px; width: 120px; height: 18px; background: #222; clip-path: polygon(10% 0, 90% 0, 100% 100%, 0 100%); display: flex; justify-content: center; align-items: center; gap: 8px; }
  .hero-pager span { width: 7px; height: 7px; border-radius: 50%; background: #777; }
  .hero-pager span.on { background: #fff; }

  .support-tab { position: absolute; left: 118px; top: 262px; width: 44px; height: 132px; background: linear-gradient(90deg, #c8c8c8, var(--tab)); border-radius: 0 6px 6px 0; box-shadow: 1px 1px 4px rgba(0,0,0,.35); }
  .support-tab span { position: absolute; left: 50%; top: 50%; transform: translate(-50%, -50%) rotate(-90deg); white-space: nowrap; text-align: center; color: #444; font-size: 14px; line-height: 1.15; }
  .support-tab b { display: block; font-size: 16px; color: #222; }

  .columns { position: absolute; top: 348px; left: 200px; right: 200px; display: grid; grid-template-columns: 250px 250px 250px; gap: 25px; }
  .columns h3 { font-size: 16px; font-weight: 400; color: var(--ink); margin-bottom: 10px; }
  .columns h3 em { font-style: normal; color: var(--brand-blue); font-weight: 700; }
  .columns h3 strong { color: var(--ink); }
  .columns p { font-size: 11px; line-height: 1.5; color: var(--muted); text-align: justify; }
  .client-photo { width: 140px; height: 70px; border: 2px solid #fff; box-shadow: 0 1px 3px rgba(0,0,0,.35); background: linear-gradient(110deg, #6e7d8e, #b4aea0 55%, #857c6f); margin-bottom: 6px; }
  .enquiry { display: grid; grid-template-columns: 1fr 1fr; gap: 7px; }
  .enquiry .field { height: 19px; border-radius: 10px; background: var(--field); border: 1px solid var(--field-edge); box-shadow: inset 0 1px 2px rgba(0,0,0,.15); font-size: 10.5px; font-style: italic; color: #555; padding: 3px 10px; }
  .enquiry .wide { grid-column: 1 / 3; width: 150px; }
  .enquiry .message { grid-column: 1 / 3; }
</style>
</head>
<body>
  <div class="top-rule"></div>

  <header class="site-header">
    <div class="brand">
      <span class="brand-name">Marlcombe Electrical Services</span>
      <span class="brand-tagline">Careful Work, Lasting Standards</span>
    </div>

    <div class="callback">
      <p>Enter your number and we will call you<br>to answer any questions</p>
      <div class="callback-row">
        <span class="callback-field short"></span>
        <span class="callback-field short"></span>
        <span class="callback-field long"></span>
        <span class="callback-btn">
          <svg width="20" height="16" viewBox="0 0 20 16" aria-label="Call me">
            <path d="M2 5 C2 1 18 1 18 5 L15 7 L13 5 L7 5 L5 7 Z" fill="#333"/>
            <rect x="4" y="8" width="12" height="7" rx="1.5" fill="#333"/>
            <circle cx="10" cy="11.5" r="2" fill="#d6d6d6"/>
          </svg>
        </span>
      </div>
    </div>
  </header>

  <nav class="main-nav">
    <a class="active" href="#">HOME</a>
    <a href="#">ABOUT US</a>
    <a href="#">SERVICES</a>
    <a href="#">QUALITY</a>
    <a href="#">OUR CLIENTS</a>
    <a href="#">CONTACT US</a>
  </nav>

  <div class="hero-band"></div>
  <section class="hero">
    <div class="hero-photo" role="img" aria-label="Electrician in hard hat and hi-vis vest working on a distribution board"></div>
    <div class="hero-caption">
      <h2>Superior Quality!</h2>
      <p>We promise our customers to continue to provide superior quality; whether in products, services, or workmanship. <a href="#">Find out more about our commitment to our customers.</a></p>
    </div>
  </section>
  <div class="hero-pager"><span class="on"></span><span></span><span></span><span></span></div>

  <aside class="support-tab"><span>Support &amp; Service<b>OFFLINE</b></span></aside>

  <main class="columns">
    <section>
      <h3><em>Welcome</em> to <strong>MARLCOMBE</strong></h3>
      <p>Marlcombe Electrical Services Ltd is a well-established business whose workers have combined industry experience of over 30 years providing a first class reliable service in all fields of electrical contracting. We are pleased to offer advice over the telephone on various aspects of electrical installations relating to regulations. We offer free quotations.</p>
    </section>
    <section>
      <h3><em>Committed</em> to Our Clients</h3>
      <div class="client-photo" role="img" aria-label="Two electricians inspecting an electrical panel"></div>
      <p>Lorem ipsum dolor sit amet, consectetur adipiscing elit. Phasellus posuere neque at massa tincidunt.</p>
    </section>
    <section>
      <h3><em>How</em> Can We Help You?</h3>
      <form class="enquiry">
        <div class="field">First Name...</div>
        <div class="field">Last Name...</div>
        <div class="field wide">Company...</div>
        <div class="field wide">E-mail Address...</div>
        <div class="field wide">Phone Number...</div>
        <div class="field message">What can we help with?</div>
      </form>
    </section>
  </main>
</body>
</html>
```